Margot Vellacott Designs

- Interior design consultant
- Want a monogram/logo at the top within a circle similar to tallowmerestudio.com.au
- Want the colors, font, theme, layout to be similar to tallowmerestudio.com.au
- Monogram possibly in the gold circle/leaf thing as visible on the attached pictures, maybe a MV with a backwards "E" within a circle
- Black background, white writing
- 1 side an enlarge logo with nothing else, other side to have a small logo at top with company name, mobile and email below

Industry/Entity Type

It Company

Contact Information for Business Card

Company name: Margot Vellacott Interiors
Mobile: 0481 356 914
Email: margotvellacott@quillpost.com

Colors
000000
ffffff

```html
<!DOCTYPE html>
<html lang="en">
<head>
<meta charset="utf-8">
<title>Margot Vellacott Interiors – Business Card</title>
<link rel="stylesheet" href="https://fonts.googleapis.com/css2?family=Pinyon+Script&family=EB+Garamond:wght@400&family=Playfair+Display:wght@400&display=swap">
<style>
  :root {
    --backdrop: #dcd8d1;
    --card: #000000;
    --ink: #ffffff;
    --gold: #a8996a;
    --card-w: 600px;
    --card-h: 343px;
  }
  * { box-sizing: border-box; margin: 0; padding: 0; }
  html, body {
    width: 1200px;
    height: 1000px;
    overflow: hidden;
    background: var(--backdrop);
  }
  .canvas {
    position: relative;
    width: 1200px;
    height: 1000px;
  }
  .card {
    position: absolute;
    left: 300px;
    width: var(--card-w);
    height: var(--card-h);
    background: var(--card);
    color: var(--ink);
    box-shadow: 0 6px 18px rgba(0, 0, 0, 0.25);
  }
  .card--front { top: 110px; }
  .card--back { top: 547px; }
  .card__frame {
    position: absolute;
    inset: 14px;
    border: 1px solid var(--gold);
  }
  .monogram {
    position: absolute;
    left: 50%;
    transform: translateX(-50%);
    display: flex;
    align-items: center;
    justify-content: center;
    border: 2px solid var(--gold);
    border-radius: 50%;
    font-family: "Playfair Display", serif;
    font-weight: 400;
    color: var(--ink);
    letter-spacing: 0.02em;
  }
  .monogram--small {
    top: 46px;
    width: 64px;
    height: 64px;
    font-size: 18px;
  }
  .monogram--large {
    top: 50%;
    transform: translate(-50%, -50%);
    width: 180px;
    height: 180px;
    font-size: 44px;
    border-width: 3px;
  }
  .company-name {
    position: absolute;
    top: 126px;
    left: 0;
    right: 0;
    text-align: center;
    font-family: "Pinyon Script", cursive;
    font-size: 44px;
    font-weight: 400;
    color: var(--ink);
  }
  .contact {
    position: absolute;
    bottom: 42px;
    left: 0;
    right: 0;
    text-align: center;
    font-family: "EB Garamond", serif;
    font-size: 17px;
    color: var(--ink);
    letter-spacing: 0.01em;
  }
  .contact__sep {
    margin: 0 6px;
  }
</style>
</head>
<body>
  <main class="canvas">
    <section class="card card--front" aria-label="Business card front">
      <div class="card__frame"></div>
      <div class="monogram monogram--small">MV</div>
      <h1 class="company-name">Margot Vellacott Interiors</h1>
      <p class="contact">
        Mobile: 0481 356 914<span class="contact__sep">&bull;</span>Email: margotvellacott@quillpost.com
      </p>
    </section>

    <section class="card card--back" aria-label="Business card back">
      <div class="card__frame"></div>
      <div class="monogram monogram--large">MV</div>
    </section>
  </main>
</body>
</html>
```